Beauty Salon Treatment Menu & Pricing

We need a Treatment Pricelist/ Brochure made to hand out to potential & existing customers! Meadowlark Body & Makeup is a small friendly beauty salon focused on the beauty essentials such as waxing, spray tanning, facials & makeup. We have a webpage with our colour theme and style and we would like to brochure to tie in.
www.meadowlarkbodyandmakeup.com.au.
We like a brochure that is clean, simple and easy to read.

Industry/Entity Type

Beauty Salon

```html
<!DOCTYPE html>
<html lang="en">
<head>
<meta charset="utf-8">
<title>Meadowlark Body &amp; Makeup – Treatment Menu</title>
<link href="https://fonts.googleapis.com/css2?family=Open+Sans:wght@300;400;600&display=swap" rel="stylesheet">
<style>
:root{
  --bg:#e9455c;
  --bg-deep:#d93a52;
  --ink:#ffffff;
  --ink-soft:rgba(255,255,255,0.72);
  --skin-light:#f3d6c8;
  --skin-mid:#d9a994;
}
*{margin:0;padding:0;box-sizing:border-box}
html,body{width:710px;height:1200px;overflow:hidden}
body{background:var(--bg);font-family:"Open Sans",Arial,sans-serif;color:var(--ink)}
.menu{position:relative;width:710px;height:1200px;background:radial-gradient(ellipse at 50% 40%,var(--bg) 0%,var(--bg-deep) 100%)}
.price-list{position:absolute;left:34px;width:281px}
.section-title{text-align:center;font-size:13.5px;font-weight:400;line-height:16px;letter-spacing:.3px}
.row{display:flex;justify-content:space-between;align-items:baseline;font-size:14px;font-weight:600;white-space:nowrap}
.row .price{font-weight:400;font-size:14px}
.note{font-size:7px;font-weight:400;color:var(--ink-soft)}
.facials{position:absolute;left:347px;width:323px;top:52px;height:700px}
.facials .head{text-align:center;font-size:13.5px;font-weight:400;line-height:16px}
.facial{position:absolute;left:0;width:323px}
.facial .title{display:flex;justify-content:space-between;font-size:14px;font-weight:600;line-height:17px}
.facial p{font-size:6.6px;line-height:8.4px;color:var(--ink-soft);margin-top:1px}
.addons{position:absolute;left:358px;width:297px;top:771px}
.addons .head{font-size:14px;font-weight:600;line-height:17px}
.addons .head .note{font-size:7px}
.addon{display:flex;justify-content:space-between;align-items:flex-start;font-size:14px;font-weight:600;line-height:16.5px}
.addon .name{width:210px}
.brand{position:absolute;left:0;width:710px;top:1066px;text-align:center}
.brand .name{font-size:40px;font-weight:300;letter-spacing:7px;line-height:46px}
.brand .sub{font-size:15px;font-weight:300;letter-spacing:5px;margin-top:4px}
.photo{position:absolute}
.photo-left{left:0;top:1008px;width:156px;height:192px;border-radius:0 90px 0 0;background:radial-gradient(ellipse at 40% 45%,var(--skin-light) 0%,var(--skin-mid) 55%,#6b4a3e 100%)}
.photo-right{right:0;top:1032px;width:182px;height:168px;border-radius:90px 0 0 0;background:radial-gradient(ellipse at 55% 60%,#fbf3ef 0%,var(--skin-light) 50%,#f4e9e5 100%)}
</style>
</head>
<body>
<main class="menu">

  <section class="price-list" style="top:52px">
    <h2 class="section-title" style="margin-bottom:3px">FACIAL WAXING/ TINT</h2>
    <div style="line-height:16.6px">
      <div class="row"><span>Eyebrow</span><span class="price">18.00</span></div>
      <div class="row"><span>Brow wax &amp; tint</span><span class="price">30.00</span></div>
      <div class="row"><span>Lip or chin or sides</span><span class="price">10.00</span></div>
      <div class="row"><span>Brow, lip &amp; chin</span><span class="price">33.00</span></div>
      <div class="row"><span>Full Face</span><span class="price">38.00</span></div>
      <div class="row"><span>Lash tint</span><span class="price">20.00</span></div>
      <div class="row"><span>Brow tint</span><span class="price">16.00</span></div>
      <div class="row"><span>Lash &amp; Brow tint</span><span class="price">30.00</span></div>
    </div>
  </section>

  <section class="price-list" style="top:214px">
    <h2 class="section-title" style="margin-bottom:1px">FEMALE WAXING</h2>
    <div style="line-height:16.7px">
      <div class="row"><span>Brazilian</span><span class="price">45.00</span></div>
      <div class="row"><span>Extended Bik</span><span class="price">30.00</span></div>
      <div class="row"><span>Basic Bikini</span><span class="price">18.00</span></div>
      <div class="row"><span>Full leg</span><span class="price">45.00</span></div>
      <div class="row"><span>Full Leg &amp; Basic Bikini</span><span class="price">50.00</span></div>
      <div class="row"><span>¾ Leg</span><span class="price">35.00</span></div>
      <div class="row"><span>¾ Leg &amp; Basic Bikini</span><span class="price">45.00</span></div>
      <div class="row"><span>Half Leg (inc knees)</span><span class="price">30.00</span></div>
      <div class="row"><span>Full Arm</span><span class="price">30.00</span></div>
      <div class="row"><span>Half Arm</span><span class="price">25.00</span></div>
      <div class="row"><span>Underarm</span><span class="price">18.00</span></div>
      <div class="row"><span>Stomach</span><span class="price">15.00</span></div>
      <div class="row"><span>Back</span><span class="price">20.00</span></div>
      <div class="row"><span>Patches, from</span><span class="price">10.00</span></div>
    </div>
  </section>

  <section class="price-list" style="top:480px">
    <h2 class="section-title" style="margin-bottom:2px">MENS WAXING</h2>
    <div style="line-height:16.7px">
      <div class="row"><span>Neck</span><span class="price">25.00</span></div>
      <div class="row"><span>Back (includes neck)</span><span class="price">40.00</span></div>
      <div class="row"><span>Chest</span><span class="price">35.00</span></div>
      <div class="row"><span>Chest &amp; Stomach</span><span class="price">40.00</span></div>
      <div class="row"><span>Back, Chest &amp; Stomach</span><span class="price">75.00</span></div>
      <div class="row"><span>Full Leg</span><span class="price">55.00</span></div>
      <div class="row"><span>Full Arm</span><span class="price">38.00</span></div>
      <div class="row"><span>Underarm</span><span class="price">20.00</span></div>
    </div>
  </section>

  <section class="price-list" style="top:640px">
    <h2 class="section-title" style="margin-bottom:1px">TANNING</h2>
    <div style="line-height:17px;padding-left:4px">
      <div class="row"><span>Spray Tan <span class="note">(every 10th tan free)</span></span><span class="price">35.00</span></div>
      <div class="row"><span>Half Body Spray Tan</span><span class="price">25.00</span></div>
    </div>
  </section>

  <section class="price-list" style="top:707px">
    <h2 class="section-title" style="margin-bottom:1px">NAILS</h2>
    <div style="line-height:16.7px;padding-left:4px">
      <div class="row"><span>Manicure</span><span class="price">40.00</span></div>
      <div class="row"><span>Gel Colour Gloss Manicure</span><span class="price">50.00</span></div>
      <div class="row"><span>Mini Manicure (file &amp; polish)</span><span class="price">30.00</span></div>
      <div class="row"><span>Gel Polish Removal</span><span class="price">15.00</span></div>
    </div>
  </section>

  <section class="price-list" style="top:818px">
    <h2 class="section-title" style="margin-bottom:18px">MAKEUP</h2>
    <div style="line-height:16.2px">
      <div class="row"><span>Bridal <span class="note">(we come to you, min 3 faces, includes lashes)</span></span><span class="price">95.00</span></div>
      <div class="row"><span>Bridal Trial <span class="note">(includes take home lip colour)</span></span><span class="price">100.00</span></div>
      <div class="row"><span>Special Occasion</span><span class="price">100.00</span></div>
      <div class="row"><span>School Ball</span><span class="price">65.00</span></div>
      <div class="row"><span>False Lash Application <span class="note">(includes lashes)</span></span><span class="price">25.00</span></div>
    </div>
  </section>

  <section class="facials">
    <h2 class="head">FACIALS</h2>
    <article class="facial" style="top:18px"><div class="title"><span>Quick Fix My Skin</span><span>65.00</span></div>
      <p>Allow 30 minutes. Skin acting up? This express facial uses a blend of active products chosen to treat your current skin condition, with exfoliation, serums and a calming finishing mask.</p></article>
    <article class="facial" style="top:88px"><div class="title"><span>Glycolic Peel Treatment</span><span>55.00</span></div>
      <p>Buy 4 and get the 5th treatment free (1 treatment p/w). Allow 20 minutes. Glycolic acid and vitamin C refine tone and texture, fade pigmentation and help clear blocked pores and blemishes.</p></article>
    <article class="facial" style="top:163px"><div class="title"><span>Glycolic Microdermabrasion Treatment</span><span>100.00</span></div>
      <p>Allow 45 minutes. A highly active treatment to target skin imperfections and overall complexion. A microdermabrasion scrub and refining mask boost the glycolic peel and extend its results. Relaxing and effective.</p></article>
    <article class="facial" style="top:246px"><div class="title"><span>Clear Skin Facial</span><span>80.00</span></div>
      <p>Allow 45 mins. A deep cleansing facial designed to help manage and treat oily, acne and pustular skin, using vitamin A, tea tree, fruit acids, minerals and deep cleansing clays.</p></article>
    <article class="facial" style="top:310px"><div class="title"><span>Rebalancing Vitamin A Facial</span><span>90.00</span></div>
      <p>Allow 60 mins. A relaxing treatment for combination skin types, to detox, purify and heal the skin with vitamin A, zinc oxide, lotus flower, green tea and ginkgo biloba.</p></article>
    <article class="facial" style="top:374px"><div class="title"><span>Marine Radiance Facial</span><span>100.00</span></div>
      <p>Allow 60 mins. This gentle, rehydrating treatment suits most skin types, restoring softness and radiance with oxygenating marine extracts, collagen and elastin. A perfect facial for the bride-to-be (add a glycolic peel to enhance the benefits).</p></article>
    <article class="facial" style="top:450px"><div class="title"><span>Anti Stress, Sensitive<br>Skin Treatment</span><span>100.00</span></div>
      <p>Allow 60 mins. Perfect for skin prone to redness, irritation, flakiness and inflammation. Super relaxing, using soothing plant extracts and calming actives. Great for anyone with eczema, dermatitis or psoriasis. Skin will look and feel calmer.</p></article>
    <article class="facial" style="top:543px"><div class="title"><span>Anti Ageing Hydra<br>Restore Facial</span><span>120.00</span></div>
      <p>Allow 60 mins. A beautiful hot oil infusion treatment using 100% natural vitamins and oils. Great for signs of dehydration, dryness and wrinkles. Skin will look younger, healthier and radiant. Perfect after a course of glycolic peels.</p></article>
    <article class="facial" style="top:625px"><div class="title"><span>Firming Lift Facial</span><span>150.00</span></div>
      <p>Allow 60 mins. Our most luxurious and restorative facial to firm, strengthen and oxygenate the skin with marine collagen, elastin and pearl extract. Ideal for skin losing firmness and elasticity, and for delicate, fragile skin. Includes caviar &amp; pearl eye treatment.</p></article>
  </section>

  <section class="addons">
    <h3 class="head">FACIAL ADD ONS <span class="note">(Incorporate any of the following into your facial treatment for a small cost)</span></h3>
    <div class="addon" style="margin-top:12px"><span class="name">Glycolic Peel</span><span>$20</span></div>
    <div class="addon" style="margin-top:17px"><span class="name">Firming Lift Caviar &amp; Pearl Eye Treatment</span><span>$20</span></div>
    <div class="addon" style="margin-top:0"><span class="name">Firming Lift Neck &amp; Bust Treatment</span><span>$20</span></div>
    <div class="addon" style="margin-top:0"><span class="name">Mini Pedicure <span style="font-size:8px">(file &amp; Polish)</span></span><span>$30</span></div>
  </section>

  <div class="photo photo-left" role="img" aria-label="Photo of a relaxed client with a flower in her hair resting on a towel"></div>
  <div class="photo photo-right" role="img" aria-label="Photo of smooth bare legs and feet with painted toenails"></div>

  <footer class="brand">
    <div class="name">MEADOWLARK</div>
    <div class="sub">BODY &amp; MAKEUP</div>
  </footer>

</main>
</body>
</html>
```